General Contractors need a new Crisp updated Card Design

We need a new business card design for our company of 25 years based in Toronto call Holvaster Building Inc. : Our goal is to be the leading commercial contractors in Toronto by providing exceptional value to our clients. We work very hard to deliver professional, quality, service in conjunction with consistent price competitiveness to all of our clients on every single project.

Target Market(s)

Design & Build Clients

Industry/Entity Type

Construction Company

Contact Information for Business Card

Address:
18 North Tamlin Glen Road, Unit 57, Marbrook Vale, ON, K7T 2R9
Office: 905-218-5937

Holvasters Logo
Employee Job Description
Employee Cell Phone #
Employee Email
www.holvaster-example.com

Colors

Designer to choose colors to be used in the design.

Requirements
Must have
• Quote Company Saying:
• "Professional. Quality. Service."
Nice to have
• New Crisp up to date look. simple & fresh ( Not to Busy)
Should not have
• NO BLUE PRINTS ON THE BUSINESS CARDS

```html
<!DOCTYPE html>
<html lang="en">
<head>
<meta charset="utf-8">
<title>Holvaster Building Inc. – Business Card</title>
<link href="https://fonts.googleapis.com/css2?family=Exo+2:wght@400;500;600&display=swap" rel="stylesheet">
<style>
  :root {
    --backdrop: #02776c;
    --brand-teal: #047a6e;
    --card-white: #ffffff;
    --ink: #333333;
  }
  * { margin: 0; padding: 0; box-sizing: border-box; }
  html, body {
    width: 1200px; height: 900px; overflow: hidden;
    background: var(--backdrop);
    font-family: "Exo 2", Arial, sans-serif;
  }
  .canvas { position: relative; width: 1200px; height: 900px; }

  .card { position: absolute; }

  /* Front */
  .card-front {
    left: 300px; top: 78px; width: 603px; height: 343px;
    background: var(--brand-teal);
    color: var(--card-white);
    display: flex; flex-direction: column; align-items: center; justify-content: center;
    padding-top: 10px;
  }
  .brand {
    display: flex; align-items: center; gap: 12px;
    font-weight: 500; white-space: nowrap;
  }
  .brand-mark { display: block; flex: none; background: currentColor; }
  .card-front .brand { font-size: 31px; }
  .card-front .brand-mark { width: 30px; height: 30px; }
  .card-front .tagline {
    margin-top: 22px; font-size: 20px; font-weight: 500; letter-spacing: 0.3px;
  }

  /* Back */
  .card-back {
    left: 294px; top: 477px; width: 611px; height: 348px;
    background: var(--card-white);
  }
  .company-block {
    position: absolute; right: 34px; top: 26px;
    color: var(--brand-teal);
  }
  .card-back .brand { font-size: 22px; justify-content: flex-end; height: 52px; }
  .card-back .brand-mark { width: 22px; height: 22px; }
  .card-back .tagline {
    margin-top: 8px; font-size: 15px; font-weight: 600; letter-spacing: 0.4px; white-space: nowrap;
  }
  .address { margin-top: 10px; font-size: 14px; line-height: 16px; }

  .person { position: absolute; left: 39px; top: 149px; right: 34px; }
  .person-name { font-size: 22px; font-weight: 500; color: var(--brand-teal); line-height: 26px; }
  .person-role-row { display: flex; align-items: center; gap: 10px; margin-top: 1px; }
  .person-role { font-size: 12px; color: var(--ink); white-space: nowrap; }
  .rule { flex: 1; height: 2px; background: var(--brand-teal); }

  .contact-list {
    position: absolute; left: 39px; top: 202px; list-style: none;
  }
  .contact-list li {
    display: flex; align-items: center; height: 26.5px;
    font-size: 14px; color: var(--ink);
  }
  .contact-list svg { width: 20px; height: 20px; margin-right: 13px; fill: var(--brand-teal); }
</style>
</head>
<body>
<div class="canvas">

  <section class="card card-front" aria-label="Card front">
    <div class="brand"><span class="brand-mark"></span>Holvaster Building Inc.</div>
    <p class="tagline">Professional . Quality . Service</p>
  </section>

  <section class="card card-back" aria-label="Card back">
    <div class="company-block">
      <div class="brand"><span class="brand-mark"></span>Holvaster Building Inc.</div>
      <p class="tagline">Professional . Quality . Service</p>
      <p class="address">18 North Tamlin Glen Road, Unit 57,<br>Marbrook Vale, ON, K7T 2R9</p>
    </div>

    <div class="person">
      <h1 class="person-name">Marcus Delaney</h1>
      <div class="person-role-row">
        <span class="person-role">CEO | Founder</span>
        <span class="rule"></span>
      </div>
    </div>

    <ul class="contact-list">
      <li>
        <svg viewBox="0 0 24 24" aria-hidden="true"><path d="M6.6 10.8a15.1 15.1 0 0 0 6.6 6.6l2.2-2.2c.3-.3.7-.4 1-.2 1.1.4 2.3.6 3.6.6.6 0 1 .4 1 1V20c0 .6-.4 1-1 1A17 17 0 0 1 3 4c0-.6.4-1 1-1h3.5c.6 0 1 .4 1 1 0 1.3.2 2.5.6 3.6.1.3 0 .7-.2 1z"/></svg>
        905-218-5937
      </li>
      <li>
        <svg viewBox="0 0 24 24" aria-hidden="true"><path d="M7 2h10a1 1 0 0 1 1 1v18a1 1 0 0 1-1 1H7a1 1 0 0 1-1-1V3a1 1 0 0 1 1-1zm1 2v7h8V4zm0 9v2h2v-2zm3 0v2h2v-2zm3 0v2h2v-2zm-6 3v2h2v-2zm3 0v2h2v-2zm3 0v2h2v-2z"/></svg>
        905-218-5937
      </li>
      <li>
        <svg viewBox="0 0 24 24" aria-hidden="true"><path d="M2 5h20v14H2zm2 2v.4l8 5.2 8-5.2V7zm0 2.8V17h16V9.8l-8 5.2z"/></svg>
        delaney@holvaster-example.com
      </li>
      <li>
        <svg viewBox="0 0 24 24" aria-hidden="true"><path d="M12 2a10 10 0 1 0 0 20 10 10 0 0 0 0-20zm6.9 6h-3a15 15 0 0 0-1.3-3.9A8 8 0 0 1 18.9 8zM12 4c.8 1.2 1.5 2.5 1.9 4h-3.8c.4-1.5 1.1-2.8 1.9-4zM4.3 14a8 8 0 0 1 0-4h3.4a16 16 0 0 0 0 4zm.8 2h3a15 15 0 0 0 1.3 3.9A8 8 0 0 1 5.1 16zm3-8h-3a8 8 0 0 1 4.3-3.9C8.8 5.3 8.4 6.6 8.1 8zM12 20c-.8-1.2-1.5-2.5-1.9-4h3.8c-.4 1.5-1.1 2.8-1.9 4zm2.3-6H9.7a14 14 0 0 1 0-4h4.6a14 14 0 0 1 0 4zm.3 5.9c.6-1.2 1-2.5 1.3-3.9h3a8 8 0 0 1-4.3 3.9zM16.3 14a16 16 0 0 0 0-4h3.4a8 8 0 0 1 0 4z"/></svg>
        www.holvaster-example.com
      </li>
    </ul>
  </section>

</div>
</body>
</html>
```